Stationery Set for BRV Company

I need to create full stationery design for my company; Business Cards, Envelops, Letter Heads, Calendar.
In the letter head and Envelops... only contact information and website links.
Our company is a Service Management company with different domains of innovative services including Technology Service Management, Education Services, Outsourcing Management, Events Management.
I need a modern and innovative design specially for the business card. I some transparent designs and I like it, but don't limit your innovation to what I mentioned. Sky is limit for your innovation.

Target Market(s)

Middle East & Africa

Industry/Entity Type

Business Management

Colors
34a7d8
0355a3
85acd3
86cae7
cee9f5
cfdeed
e4daeb
f3f1f8
ecf7fb

Requirements
Must have
• Name, Title, Email, Mobile
Nice to have
• We have multiple locations in USA, KSA, EGY, so I need ideas about how to include all contact details maybe QR / Barcode or something else.
• Please see our locations and contact information: www.ploventa.com
Should not have
• Too much text

```html
<!DOCTYPE html>
<html lang="en">
<head>
<meta charset="utf-8">
<title>BRV Company – Business Cards</title>
<link rel="stylesheet" href="https://fonts.googleapis.com/css2?family=Open+Sans:wght@400;600;700&display=swap">
<style>
  :root{
    --bg:#e9e8ec;
    --card:#ffffff;
    --brand-blue:#0355a3;
    --mid-blue:#3f73c6;
    --light-blue:#6a94d6;
    --band-grey:#d7d5d8;
    --text-grey:#7d7b80;
    --text-dark:#2b2b2e;
    --white:#ffffff;
  }
  *{box-sizing:border-box;margin:0;padding:0}
  html,body{width:1200px;height:950px;overflow:hidden}
  body{background:var(--bg);font-family:"Open Sans",Arial,sans-serif;position:relative}

  .card{position:absolute;width:700px;height:400px;background:var(--card);
        box-shadow:0 10px 28px rgba(0,0,0,.18);overflow:hidden}
  .card--front{left:110px;top:45px}
  .card--back{left:390px;top:505px}

  .brand{display:flex;align-items:center;justify-content:center;gap:12px}
  .brand__dot{width:22px;height:22px;border-radius:50%;background:var(--brand-blue)}
  .brand__name{font-weight:700;font-size:40px;color:var(--brand-blue);letter-spacing:.5px}

  .card--front .brand{position:absolute;left:0;right:0;top:140px}
  .front__web{position:absolute;left:0;right:0;top:250px;text-align:center;
              font-size:17px;font-weight:600;letter-spacing:2px;color:var(--text-dark)}

  .card--back .brand{position:absolute;left:0;right:0;top:70px}
  .back__band{position:absolute;left:0;right:0;top:190px;height:58px;background:var(--band-grey);
              display:flex;align-items:center;justify-content:center;gap:8px}
  .person__name{font-size:22px;font-weight:700;color:var(--mid-blue)}
  .person__title{font-size:16px;color:var(--text-grey)}

  .back__info{position:absolute;left:0;right:0;top:248px;bottom:0;
              background:linear-gradient(100deg,var(--mid-blue) 0%,var(--light-blue) 55%,var(--mid-blue) 100%);
              display:flex;gap:30px;padding:22px 34px;color:var(--white);font-size:13px;line-height:1.5}
  .office{flex:1}
  .office__label{font-weight:700;font-size:14px;text-transform:uppercase;margin-bottom:2px}
  .office strong{font-weight:700}
  .contacts{flex:1;list-style:none;display:flex;flex-direction:column;gap:8px;padding-top:4px}
  .contacts li{display:flex;align-items:center;gap:10px}
  .contacts svg{width:16px;height:16px;flex:none}
</style>
</head>
<body>

  <section class="card card--front" aria-label="Business card front">
    <div class="brand"><span class="brand__dot"></span><span class="brand__name">BRV Company</span></div>
    <p class="front__web">www.ploventa.com</p>
  </section>

  <section class="card card--back" aria-label="Business card back">
    <div class="brand"><span class="brand__dot"></span><span class="brand__name">BRV Company</span></div>

    <div class="back__band">
      <span class="person__name">Omar Haddad</span>
      <span class="person__title">- CEO/Founder</span>
    </div>

    <div class="back__info">
      <div class="office">
        <p class="office__label">Saudi Arabia:</p>
        <p>Riyadh, Al Nakheel,<br>King Fahd Branch Rd.<br>Al Noor Buildings<br>Block 3A 1st Floor B12, B14<br><strong>Phone :</strong> +966 55501 20 30</p>
      </div>
      <div class="office">
        <p class="office__label">USA:</p>
        <p>418 Harbor Point Avenue<br>4th Floor Bayview City<br>CA 94100 US<br><strong>Phone:</strong>+1.5550142870</p>
      </div>
      <ul class="contacts">
        <li>
          <svg viewBox="0 0 16 16" aria-hidden="true"><rect x="4" y="1" width="8" height="14" rx="1.5" fill="none" stroke="#fff" stroke-width="1.4"/><circle cx="8" cy="12.5" r=".9" fill="#fff"/></svg>
          +1.5550142870
        </li>
        <li>
          <svg viewBox="0 0 16 16" aria-hidden="true"><rect x="1" y="3" width="14" height="10" rx="1" fill="none" stroke="#fff" stroke-width="1.4"/><path d="M1.5 3.5 8 9l6.5-5.5" fill="none" stroke="#fff" stroke-width="1.4"/></svg>
          info@ploventa.com
        </li>
        <li>
          <svg viewBox="0 0 16 16" aria-hidden="true"><circle cx="8" cy="8" r="6.5" fill="none" stroke="#fff" stroke-width="1.4"/><path d="M1.5 8h13M8 1.5c-2.5 3-2.5 10 0 13M8 1.5c2.5 3 2.5 10 0 13" fill="none" stroke="#fff" stroke-width="1.1"/></svg>
          www.ploventa.com
        </li>
      </ul>
    </div>
  </section>

</body>
</html>
```